KLD Photography Editing & Support Services for Real Estate

We require a double sided A4 flyer to promote our photography services to real estate agencies.
This particular service is targeted to rural areas where reliable, professional and highly skilled photographers are difficult to source. We teach the agent how to photograph, they upload files to a server and we take care of the rest (image editing, quality control and delivery). This will give the agents flexibility with when to shoot and eliminates the stress of managing a photographer / contractor. We offer a 1 day face to face training session and competitive packages for equipment start up.
We would like the flyer to look clean & very professional. The flyer should showcase samples of our work to highlight what can be achieved by using our services. We like the look of a black or dark background behind the text and feel that would look nice with our photographs provided. Otherwise open to your suggestions and ideas.
TEXT FOR FLYER:
Welcome to the KLD Real Estate Photography Editing and Support Service
• Take your real estate business to the next level by providing impressive real estate imagery that makes you stands out from the competition
• Omit the stress of trying to find a good photographer or managing an unreliable one and hence have more time to focus on other aspects of your business
• Showcase your listings with better quality and more impactful photographs than your competitors thereby increasing potential for a quick sale
• Great first impressions matter and you will achieve this by looking and feeling more professional. This will attract and retain more future clients.
HOW IT WORKS
• We understand that your time is valuable, so let us handle the editing and delivery of your images. You shoot, and we take care of the rest.
• Images are edited and delivered within 1 working day
INCLUSIONS:
• Full day face to face training (we come to you) and instructional handbook
• We will teach you everything you need to know about your equipment and how to take stunning real estate photographs
• Service turnaround within 1 working day
• Free HELP desk service Mon-Fri
• 12 month Exclusivity (rural towns only) for a limited time
INVESTMENT
• 99 per listing for us to manage images including editing, quality control and delivery (10 Images)
• Ask us about competitive packages for photography equipment if required
SUMMARY
The KLD Real Estate Photography Editing and Support Service is the perfect solution for busy real estate professionals who want to take their business to the next level. Our service is affordable, flexible, and designed to help you showcase your listings in the best possible light.
Contact us today to learn more about how we can help you.

```html
<!DOCTYPE html>
<html lang="en">
<head>
<meta charset="utf-8">
<title>KLD Real Estate Photography Flyer</title>
<link rel="stylesheet" href="https://fonts.googleapis.com/css2?family=Poppins:wght@300;400;500;600;700&display=swap">
<style>
  :root {
    --stage: #676780;
    --navy: #15152b;
    --ink: #07070f;
    --white: #ffffff;
    --muted: #b9bccb;
    --accent: #2aa8e0;
  }
  * { margin: 0; padding: 0; box-sizing: border-box; }
  html, body { width: 741px; height: 1200px; overflow: hidden; }
  body { background: var(--stage); font-family: "Poppins", sans-serif; color: var(--white); position: relative; }

  .page { position: absolute; top: 376px; width: 345px; height: 447px; background: var(--navy); overflow: hidden; }
  .page--front { left: 16px; }
  .page--back { left: 380px; }
  .page > * { position: absolute; }
  .shapes { left: 0; top: 0; width: 345px; height: 447px; }

  .brand { left: 5px; top: 64px; width: 200px; text-align: center; font-weight: 300; font-size: 11px; line-height: 14px; letter-spacing: 2.6px; color: var(--muted); text-transform: uppercase; }

  .welcome { left: 37px; top: 103px; font-size: 15.5px; line-height: 16px; font-weight: 700; }
  .welcome__lead { display: block; font-weight: 400; font-size: 11.5px; line-height: 14px; }
  .welcome__title { display: block; font-weight: 700; font-size: 15.5px; line-height: 16px; }

  .section-title { font-weight: 600; font-size: 13px; line-height: 16px; left: 166px; top: 244px; }

  .ticks { list-style: none; font-size: 5.8px; line-height: 1.27; text-align: justify; }
  .ticks li { position: relative; padding-left: 8px; margin-bottom: 7px; }
  .ticks li svg { position: absolute; left: 0; top: 0.5px; width: 6px; height: 6px; }
  .page--front .ticks { left: 166px; top: 264px; width: 140px; }
  .page--front .ticks li { margin-bottom: 8.5px; }

  .band-title { left: 36px; font-weight: 600; font-size: 11px; letter-spacing: 1px; line-height: 13px; }
  .band-title--how { top: 108px; }
  .band-title--inc { top: 189px; }
  .band-title--inv { top: 316px; }
  .page--back .ticks { left: 37px; width: 140px; }
  .ticks--how { top: 126px; }
  .ticks--inc { top: 207px; }
  .ticks--inv { top: 336px; }

  .summary-label { left: 225px; top: 331px; width: 71px; height: 10px; background: var(--accent); font-weight: 700; font-size: 8px; letter-spacing: 0.8px; text-align: center; line-height: 10px; }
  .summary-text { left: 224px; top: 344px; width: 74px; font-size: 4.1px; line-height: 1.28; text-align: center; }

  .contact { left: 166px; top: 418px; font-weight: 600; font-size: 6px; line-height: 1.15; }
  .contact__phone { font-size: 8px; display: flex; align-items: center; gap: 2px; }
  .contact__phone svg { width: 7px; height: 7px; }
</style>
</head>
<body>

<section class="page page--front" aria-label="Flyer front">
  <svg class="shapes" viewBox="0 0 345 447" aria-hidden="true">
    <defs>
      <linearGradient id="front-hero" x1="0" y1="0" x2="0" y2="1">
        <stop offset="0" stop-color="#5f86b8"/><stop offset="0.55" stop-color="#3a3b4c"/><stop offset="1" stop-color="#4e5a3a"/>
      </linearGradient>
      <linearGradient id="front-side" x1="0" y1="0" x2="1" y2="1">
        <stop offset="0" stop-color="#7b7fa8"/><stop offset="0.6" stop-color="#a08a6c"/><stop offset="1" stop-color="#c9c9cf"/>
      </linearGradient>
      <linearGradient id="front-room" x1="0" y1="0" x2="1" y2="0">
        <stop offset="0" stop-color="#d8d4cc"/><stop offset="1" stop-color="#8a8f84"/>
      </linearGradient>
    </defs>
    <polygon points="216,0 345,0 345,234 160,234" fill="url(#front-hero)" role="img" aria-label="Photo: cottage exterior at dusk with lit porch and gravel path"/>
    <polygon points="0,228 149,228 116,371 0,371" fill="url(#front-side)" role="img" aria-label="Photo: modern farmhouse with stone chimney at twilight"/>
    <polygon points="0,381 105,381 91,447 0,447" fill="url(#front-room)" role="img" aria-label="Photo: bright bedroom with large windows onto countryside"/>
    <line x1="156" y1="238" x2="88" y2="447" stroke="#ffffff" stroke-width="0.7"/>
    <line x1="162" y1="250" x2="98" y2="447" stroke="#ffffff" stroke-width="0.7"/>
    <polygon points="128,413 345,413 345,447 117,447" fill="var(--ink)"/>
  </svg>

  <p class="brand">Mara Ellison</p>

  <h1 class="welcome">
    <span class="welcome__lead">Welcome to the</span>
    <span class="welcome__title">KLD Real Estate<br>Photography<br>Editing and<br>Support Service</span>
  </h1>

  <h2 class="section-title">KLD Real Estate</h2>
  <ul class="ticks">
    <li><svg viewBox="0 0 10 10"><path d="M1 5.5 L4 8.5 L9 1.5" fill="none" stroke="#fff" stroke-width="1.6"/></svg>Take your real estate business to the next level by providing impressive real estate imagery that makes you stands out from the competition</li>
    <li><svg viewBox="0 0 10 10"><path d="M1 5.5 L4 8.5 L9 1.5" fill="none" stroke="#fff" stroke-width="1.6"/></svg>Omit the stress of trying to find a good photographer or managing an unreliable one and hence have more time to focus on other aspects of your business</li>
    <li><svg viewBox="0 0 10 10"><path d="M1 5.5 L4 8.5 L9 1.5" fill="none" stroke="#fff" stroke-width="1.6"/></svg>Showcase your listings with better quality and more impactful photographs than your competitors thereby increasing potential for a quick sale</li>
    <li><svg viewBox="0 0 10 10"><path d="M1 5.5 L4 8.5 L9 1.5" fill="none" stroke="#fff" stroke-width="1.6"/></svg>Great first impressions matter and you will achieve this by looking and feeling more professional. This will attract and retain more future clients.</li>
  </ul>

  <p class="contact">Contact us today to<br>learn more about how we can help you.
    <span class="contact__phone"><svg viewBox="0 0 10 10"><path d="M2.5 1 L4 3 L3 4.2 Q4.2 6 5.8 7 L7 6 L9 7.5 L8 9 Q3.5 8.5 1 2 Z" fill="#fff"/></svg>000 0000 0000</span>
  </p>
</section>

<section class="page page--back" aria-label="Flyer back">
  <svg class="shapes" viewBox="0 0 345 447" aria-hidden="true">
    <defs>
      <linearGradient id="back-living" x1="0" y1="0" x2="0" y2="1">
        <stop offset="0" stop-color="#8a6240"/><stop offset="0.3" stop-color="#2f4f86"/><stop offset="0.65" stop-color="#1c2436"/><stop offset="1" stop-color="#9c958c"/>
      </linearGradient>
      <linearGradient id="back-hall" x1="0" y1="0" x2="1" y2="0">
        <stop offset="0" stop-color="#7a6a58"/><stop offset="0.6" stop-color="#d6dbe0"/><stop offset="1" stop-color="#eef1f4"/>
      </linearGradient>
    </defs>
    <rect x="200" y="0" width="145" height="199" fill="url(#back-living)" role="img" aria-label="Photo: living room with fireplace and tall windows at dusk"/>
    <rect x="200" y="211" width="145" height="105" fill="url(#back-hall)" role="img" aria-label="Photo: hallway lined with framed pictures and a bench"/>
    <polygon points="0,109 179,109 173,121 0,121" fill="var(--ink)"/>
    <polygon points="0,190 179,190 173,202 0,202" fill="var(--ink)"/>
    <polygon points="0,317 179,317 173,330 0,330" fill="var(--ink)"/>
    <circle cx="261" cy="363" r="45" fill="var(--ink)"/>
    <polygon points="130,413 345,413 345,447 125,447" fill="var(--ink)"/>
  </svg>

  <p class="brand">Mara Ellison</p>

  <h2 class="band-title band-title--how">HOW IT WORKS</h2>
  <ul class="ticks ticks--how">
    <li><svg viewBox="0 0 10 10"><path d="M1 5.5 L4 8.5 L9 1.5" fill="none" stroke="#2aa8e0" stroke-width="1.6"/></svg>We understand that your time is valuable, so let us handle the editing and delivery of your images. You shoot, and we take care of the rest.</li>
    <li><svg viewBox="0 0 10 10"><path d="M1 5.5 L4 8.5 L9 1.5" fill="none" stroke="#2aa8e0" stroke-width="1.6"/></svg>Images are edited and delivered within 1 working day</li>
  </ul>

  <h2 class="band-title band-title--inc">INCLUSIONS:</h2>
  <ul class="ticks ticks--inc">
    <li><svg viewBox="0 0 10 10"><path d="M1 5.5 L4 8.5 L9 1.5" fill="none" stroke="#2aa8e0" stroke-width="1.6"/></svg>Full day face to face training (we come to you) and instructional handbook</li>
    <li><svg viewBox="0 0 10 10"><path d="M1 5.5 L4 8.5 L9 1.5" fill="none" stroke="#2aa8e0" stroke-width="1.6"/></svg>We will teach you everything you need to know about your equipment and how to take stunning real estate photographs</li>
    <li><svg viewBox="0 0 10 10"><path d="M1 5.5 L4 8.5 L9 1.5" fill="none" stroke="#2aa8e0" stroke-width="1.6"/></svg>Service turnaround within 1 working day</li>
    <li><svg viewBox="0 0 10 10"><path d="M1 5.5 L4 8.5 L9 1.5" fill="none" stroke="#2aa8e0" stroke-width="1.6"/></svg>Free HELP desk service Mon-Fri</li>
    <li><svg viewBox="0 0 10 10"><path d="M1 5.5 L4 8.5 L9 1.5" fill="none" stroke="#2aa8e0" stroke-width="1.6"/></svg>12 month Exclusivity (rural towns only) for a limited time</li>
  </ul>

  <h2 class="band-title band-title--inv">INVESTMENT</h2>
  <ul class="ticks ticks--inv">
    <li><svg viewBox="0 0 10 10"><path d="M1 5.5 L4 8.5 L9 1.5" fill="none" stroke="#2aa8e0" stroke-width="1.6"/></svg>99 per listing for us to manage images including editing, quality control and delivery (10 Images)</li>
    <li><svg viewBox="0 0 10 10"><path d="M1 5.5 L4 8.5 L9 1.5" fill="none" stroke="#2aa8e0" stroke-width="1.6"/></svg>Ask us about competitive packages for photography equipment if required</li>
  </ul>

  <h2 class="summary-label">SUMMARY</h2>
  <p class="summary-text">The KLD Real Estate Photography Editing and Support Service is the perfect solution for busy real estate professionals who want to take their business to the next level. Our service is affordable, flexible, and designed to help you showcase your listings in the best possible light.</p>

  <p class="contact">Contact us today to<br>learn more about how we can help you.
    <span class="contact__phone"><svg viewBox="0 0 10 10"><path d="M2.5 1 L4 3 L3 4.2 Q4.2 6 5.8 7 L7 6 L9 7.5 L8 9 Q3.5 8.5 1 2 Z" fill="#fff"/></svg>000 0000 0000</span>
  </p>
</section>

</body>
</html>
```